Unique Business Card Design

Unique Business Card design for our orthotic and prosthetic company. Our logo is on our website, color is light blue. Unique shape (artificial leg shaped, vertical, etc..) preferred. Logo, business name, individual name and basic demographics needed.

Industry/Entity Type

Business

Contact Information for Business Card

Logo, Industry, Phone # Logo, "Prosthetic & Orthotic Services" Place to add individual name and contact info

Colors
cee9f5

Requirements
Must have
• The icon must be there, placement of "Prosthetic & Orthotic Services" can be moved
Nice to have
• Like the mix of light blue, and a little darker blue. One design included the icons from my website which was a nice touch

```html
<!DOCTYPE html>
<html lang="en">
<head>
<meta charset="utf-8">
<title>Stridewell Inc – Business Card</title>
<link rel="stylesheet" href="https://fonts.googleapis.com/css2?family=Open+Sans:wght@400;600;700&family=Cormorant+Garamond:ital,wght@1,500&display=swap">
<style>
  :root {
    --brand-blue: #1673cc;
    --brand-blue-dark: #1462b0;
    --ink: #2a2a2a;
    --paper: #ffffff;
    --backdrop: #ececec;
    --edge-accent: #e8772e;
  }
  * { box-sizing: border-box; margin: 0; padding: 0; }
  html, body { width: 1200px; height: 900px; overflow: hidden; }
  body {
    background: var(--backdrop);
    font-family: "Open Sans", Arial, sans-serif;
    display: flex;
    align-items: center;
    justify-content: center;
    gap: 40px;
  }
  .card {
    position: relative;
    width: 540px;
    height: 309px;
    border-radius: 3px;
    box-shadow: 0 10px 28px rgba(0,0,0,0.14);
  }
  .card--front { background: var(--paper); color: var(--ink); }
  .card--back { background: var(--brand-blue); color: var(--paper); border-bottom: 2px solid var(--edge-accent); }

  .brand { display: flex; align-items: center; gap: 26px; }
  .brand__dot { width: 64px; height: 64px; border-radius: 50%; flex: none; }
  .card--front .brand__dot { background: var(--brand-blue); }
  .card--back .brand__dot { background: var(--paper); }
  .brand__name {
    font-weight: 600;
    font-size: 27px;
    letter-spacing: 0.5px;
    line-height: 1;
    padding-bottom: 4px;
  }
  .brand__tagline {
    font-family: "Cormorant Garamond", Georgia, serif;
    font-style: italic;
    font-weight: 500;
    font-size: 15px;
    padding: 2px 0 3px 6px;
    border-bottom: 1.5px solid currentColor;
  }
  .card--front .brand__text { color: var(--brand-blue); }

  .card--back .brand { position: absolute; left: 70px; top: 78px; }
  .card--back .web { position: absolute; left: 70px; top: 186px; font-size: 14px; }

  .card--front .brand { position: absolute; left: 52px; top: 44px; }
  .contact { position: absolute; left: 52px; top: 152px; display: flex; gap: 16px; }
  .person { text-align: right; padding-top: 20px; }
  .person__name { color: var(--brand-blue); font-weight: 700; font-size: 16px; }
  .person__role { font-size: 13px; }
  .divider { width: 1px; background: #9aa3ad; height: 56px; margin-top: 22px; }
  .lines { list-style: none; font-size: 13px; }
  .lines li { display: flex; align-items: center; gap: 8px; line-height: 1.55; }
  .lines .phone { font-weight: 700; font-size: 15px; margin-bottom: 6px; }
  .lines svg { width: 11px; height: 11px; fill: var(--brand-blue); flex: none; }
  .address { position: absolute; left: 52px; top: 248px; font-size: 13px; }
</style>
</head>
<body>
  <article class="card card--front">
    <div class="brand">
      <span class="brand__dot"></span>
      <div class="brand__text">
        <div class="brand__name">STRIDEWELL INC</div>
        <div class="brand__tagline">Prosthetic &amp; Orthotic Services</div>
      </div>
    </div>
    <div class="contact">
      <div class="person">
        <div class="person__name">Daniel Reyes</div>
        <div class="person__role">Managing Director</div>
      </div>
      <div class="divider"></div>
      <ul class="lines">
        <li class="phone">
          <svg viewBox="0 0 24 24"><path d="M6.6 10.8a15 15 0 0 0 6.6 6.6l2.2-2.2a1 1 0 0 1 1-.25 11.4 11.4 0 0 0 3.6.57 1 1 0 0 1 1 1V20a1 1 0 0 1-1 1A17 17 0 0 1 3 4a1 1 0 0 1 1-1h3.5a1 1 0 0 1 1 1c0 1.25.2 2.45.57 3.6a1 1 0 0 1-.25 1z"/></svg>
          (555) 014-2290
        </li>
        <li>
          <svg viewBox="0 0 24 24"><path d="M2 5h20v14H2z M4 7v1l8 5 8-5V7l-8 5z" fill-rule="evenodd"/></svg>
          info@stridewellinc.com
        </li>
        <li>
          <svg viewBox="0 0 24 24"><circle cx="12" cy="12" r="10"/></svg>
          www.stridewellinc.com
        </li>
      </ul>
    </div>
    <div class="address">1234, Address GoesHere, Country name , 12345</div>
  </article>

  <article class="card card--back">
    <div class="brand">
      <span class="brand__dot"></span>
      <div class="brand__text">
        <div class="brand__name">STRIDEWELL INC</div>
        <div class="brand__tagline">Prosthetic &amp; Orthotic Services</div>
      </div>
    </div>
    <div class="web">www.stridewellinc.com</div>
  </article>
</body>
</html>
```